Plumber referral program cards

We're a busy Restoration company servicing residential and commercial properties damaged by water fire and mold. We hold the standard for Excellence, Integrity and Reliability.
This business card needs to be designed to generate high quality plumbing leads through water damage referrals

FRONT: (no specific chronological order)
-Water Damage Referral program for plumbers
-We pay plumbers $800 CASH on each water damage referral everyday!
-"To us, business is personal. Which is why referrals means rewards."
-Refer and Earn• Paid same day!

- Your customer will ALWAYS receive a FREE evaluation.
Rapid Response
24 hours a day/7 days a week

BACK: (no specific chronological order)
Water extraction•plumbing leaks•slab leaks•
Sub floor drying and repairs•Sewage cleanup•supply line rupture •structural drying•overflows•mold remediation•

-Call Wet Gone next time you run into a water damage!
555-7-WET-GON

Summit Pipefitter Bonus Scheme Bonuses
-Just to show how much your referrals mean to us, Receive $100 on every referral sent, No matter what!
- Refer Wet Gone to other property service professionals, and you recieve $100 cash for every job THEY send us!

Contact us for more information
RB Morwenna
Water Damage Restoration Specialist
Phone: 555-7-WETGON
Email: Rmorwenna@ringwetgon.example
Website: www.ringwetgon.example

Target Market(s)

Plumbers

Industry/Entity Type

It Company

Contact Information for Business Card

Rapid Response

555-7-WET-GON

RB Morwenna
Phone: 555-7-WETGON

Font styles to use
Other font styles liked:
• Times etc

Colors

Designer to choose colors to be used in the design.

Requirements
Must have
• Emphasized $800 referral fee
• Eye catching & appealing
• Our company logo and color matching
• Attached files of example competitors ads

```html
<!DOCTYPE html>
<html lang="en">
<head>
<meta charset="utf-8">
<title>Wet Gone – Plumbers Referral Cards</title>
<link rel="stylesheet" href="https://fonts.googleapis.com/css2?family=Kaushan+Script&family=Open+Sans:wght@600;700;800&display=swap">
<style>
  :root {
    --navy: #0d1a45;
    --navy-deep: #07102e;
    --navy-glow: #1b2f6e;
    --paper: #ffffff;
    --backdrop: #e9e7e3;
  }
  * { box-sizing: border-box; margin: 0; padding: 0; }
  html, body { width: 1200px; height: 963px; overflow: hidden; }
  body {
    background: var(--backdrop);
    font-family: "Open Sans", Arial, sans-serif;
    color: var(--navy);
    position: relative;
  }
  .card {
    position: absolute;
    width: 720px;
    height: 411px;
    border-radius: 4px;
    box-shadow: 0 10px 28px rgba(0,0,0,.22);
    overflow: hidden;
  }
  /* ---------- front ---------- */
  .card-front { left: 60px; top: 70px; background: var(--paper); }
  .rule { position: absolute; background: var(--navy); }
  .rule-top { left: 390px; top: 28px; width: 330px; height: 3px; }
  .rule-head { left: 30px; top: 118px; width: 690px; height: 3px; }
  .rule-mid { left: 370px; top: 292px; width: 350px; height: 3px; }
  .rule-foot { left: 0; top: 318px; width: 390px; height: 3px; }

  .kicker {
    position: absolute; left: 66px; top: 14px;
    font-family: "Kaushan Script", cursive;
    font-size: 30px; color: var(--navy);
  }
  .headline {
    position: absolute; left: 46px; top: 42px;
    font-size: 56px; font-weight: 800; letter-spacing: -0.5px;
    line-height: 1; white-space: nowrap;
  }
  .perks { position: absolute; left: 0; top: 146px; list-style: none; }
  .perk {
    height: 46px; margin-bottom: 10px;
    background: var(--navy); color: var(--paper);
    font-size: 25px; font-weight: 700; letter-spacing: .5px;
    display: flex; align-items: center; padding-left: 44px;
    clip-path: polygon(0 0, calc(100% - 22px) 0, 100% 100%, 0 100%);
  }
  .perk:nth-child(1) { width: 300px; }
  .perk:nth-child(2) { width: 345px; }
  .perk:nth-child(3) { width: 390px; }

  .bonus { position: absolute; left: 400px; top: 134px; width: 310px; text-align: center; }
  .bonus-title {
    font-size: 19px; font-weight: 800; color: var(--paper);
    -webkit-text-stroke: 1px var(--navy); margin-bottom: 6px;
  }
  .bonus-list { list-style: none; font-size: 18px; font-weight: 700; line-height: 1.2; }
  .bonus-list li { margin-bottom: 6px; }
  .bonus-list li::before { content: "• "; }

  .signer { position: absolute; right: 28px; top: 300px; text-align: right; line-height: 1; }
  .signer-name { font-size: 23px; font-weight: 800; }
  .signer-role { font-size: 16px; font-weight: 600; margin-top: 2px; }

  .contacts { position: absolute; left: 30px; top: 334px; list-style: none; font-size: 15px; font-weight: 700; line-height: 1.4; }
  .contacts li { display: flex; align-items: center; gap: 7px; }
  .contacts svg { width: 13px; height: 13px; fill: var(--navy); }

  /* ---------- back ---------- */
  .card-back {
    left: 420px; top: 482px;
    background: radial-gradient(ellipse at 45% 35%, var(--navy-glow) 0%, var(--navy) 45%, var(--navy-deep) 100%);
    display: flex; align-items: center; justify-content: center; gap: 16px;
  }
  .brand-dot { width: 40px; height: 40px; border-radius: 50%; background: var(--paper); }
  .brand-name { font-size: 60px; font-weight: 800; color: var(--paper); letter-spacing: 1px; }
</style>
</head>
<body>
  <section class="card card-front" aria-label="Referral card, front">
    <div class="rule rule-top"></div>
    <p class="kicker">Water Damage</p>
    <h1 class="headline">Plumbers Referrals</h1>
    <div class="rule rule-head"></div>

    <ul class="perks">
      <li class="perk">$800/Referral</li>
      <li class="perk">FREE Evaluation</li>
      <li class="perk">Happy&nbsp; Cusomers</li>
    </ul>

    <div class="bonus">
      <p class="bonus-title">Summit Pipefitter Bonus</p>
      <ul class="bonus-list">
        <li>Refer to other Property Service, Receive $100/Job they sent us!</li>
        <li>Receive $100/referrals sent, No Matter What!</li>
      </ul>
    </div>

    <div class="rule rule-mid"></div>
    <div class="signer">
      <p class="signer-name">RB Morwenna</p>
      <p class="signer-role">CEO</p>
    </div>

    <div class="rule rule-foot"></div>
    <ul class="contacts">
      <li><svg viewBox="0 0 24 24"><path d="M6.6 10.8a15 15 0 0 0 6.6 6.6l2.2-2.2a1 1 0 0 1 1-.25 11.4 11.4 0 0 0 3.6.57 1 1 0 0 1 1 1V20a1 1 0 0 1-1 1A17 17 0 0 1 3 4a1 1 0 0 1 1-1h3.5a1 1 0 0 1 1 1c0 1.25.2 2.45.57 3.6a1 1 0 0 1-.25 1z"/></svg>555 - 7 - WETGON</li>
      <li><svg viewBox="0 0 24 24"><path d="M2 5h20v14H2zm2 2v.5l8 5 8-5V7l-8 5z"/></svg>Rmorwenna@ringwetgon.example</li>
      <li><svg viewBox="0 0 24 24"><circle cx="12" cy="12" r="10"/></svg>www.ringwetgon.example</li>
    </ul>
  </section>

  <section class="card card-back" aria-label="Referral card, back">
    <span class="brand-dot" aria-hidden="true"></span>
    <span class="brand-name">Wet Gone</span>
  </section>
</body>
</html>
```